Business Intelligence Application - Reporting Menu and Report Criteria Design

Looking for a fresh, effective and user friendly view for the menu structure and reporting criteria screen format for a business reporting application. Initial format completed, content structure is in place, but we need the 'wow' design.. as its a serious professional report/BI tool it has to fall within certain guidelines for clarity and graphics..but we want it to be slick, friendly, great user experience. There is a large amount of complex content to fit into a small space and we need it to be very inviting, modern and intuitive.. If interested, please review the attachment. We have live screens in operation, but feel these could be improved and looking forward to seeing what great creative suggestions could be made. Please review work done to date in the attached.. We are not looking for a total re-design of everything, all the basic business content/structure is there.. but tell us what we could do to improve this in terms of graphic design... particularly the criteria screens.. thanks!
Updates

Reason: Need a few more days to review designs - thanks for all submissions so far, we will make a selection shortly.

Target Market(s)

Business analysts, hotel operations teams, finance analysts hospitality industry

Industry/Entity Type

Hospitality

Coding

Coded - Design and coding required

Number of Pages Required

4 page

Font styles to use
Sans Serif
Other font styles liked:
• Candara, please see example in deck

Colors
3276b5
3176b5
0255a3
85acd3
33a6d7
cee9f5
85cae6

Requirements
Must have
• sharp clear, logical menu structure, (currently it has 'clicks to sub-menus, we need hover over, slide to sub-menus..) colour, styling.. and most focus on revision of criteria.. right now is somewhat heavy, cumbersome.. keep colour and friendly intuitive process steps.. its heavy analytical stuff.. best of luck!
Should not have
• No grey fonts on white or grey screens! many business apps are not readable or sharp.. or fonts are too small.. colourless, so please avoid that.. see our deck - sharp dark (navy) or black fonts on white, or light shading..

```html
<!DOCTYPE html>
<html lang="en">
<head>
<meta charset="utf-8">
<title>Tallyview – Admin Setup</title>
<link href="https://fonts.googleapis.com/css2?family=Roboto:wght@400;500&display=swap" rel="stylesheet">
<style>
:root{
  --navy:#031a3a;
  --navy-row:#072a55;
  --navy-icon:#06234a;
  --royal:#0255a3;
  --sky:#33a6d7;
  --header-bg:#bcbcbc;
  --content-bg:#adb0b4;
  --panel-bg:#c9c9c9;
  --panel-head:#033d75;
  --field-bg:#c4c4c4;
  --btn:#2f86b0;
  --ink:#2b2f36;
  --muted-ink:#454a52;
  --white:#ffffff;
  --footer:#071a36;
}
*{box-sizing:border-box;margin:0;padding:0}
html,body{width:1200px;height:817px;overflow:hidden}
body{position:relative;font-family:'Roboto',sans-serif;background:var(--content-bg)}
.topbar{position:absolute;left:0;top:0;width:1200px;height:84px;background:var(--header-bg)}
.topbar .welcome{position:absolute;left:766px;top:33px;font-size:15.5px;font-weight:500;color:var(--muted-ink)}
.topbar .meta{position:absolute;left:888px;top:35px;font-size:14px;color:var(--muted-ink);display:flex;align-items:center;gap:11px}
.topbar svg{display:block}
.sidebar{position:absolute;left:0;top:0;width:218px;height:817px;background:var(--navy)}
.brand{height:85px;display:flex;align-items:center;padding-left:34px}
.brand .name{font-size:25px;font-weight:500;color:var(--white);letter-spacing:.3px}
.nav-row{display:flex;height:53px;border-bottom:1px solid #031836}
.nav-row .icon{width:63px;background:var(--navy-icon);display:flex;align-items:center;justify-content:center}
.nav-row .label{flex:1;background:var(--navy-row);display:flex;align-items:center;justify-content:space-between;padding:0 16px 0 11px;color:var(--white);font-size:16px;white-space:nowrap}
.nav-row.active .icon{background:var(--sky)}
.nav-row.active .label{background:var(--royal);padding-left:14px}
.chev{width:8px;height:12px;flex:none}
.panel{position:absolute;left:276px;top:124px;width:469px;height:552px;background:var(--panel-bg);box-shadow:0 1px 3px rgba(0,0,0,.25)}
.panel-head{height:46px;background:var(--panel-head);color:#c8d6e6;font-size:20px;padding:12px 0 0 125px}
.field-label{position:absolute;left:34px;font-size:15.5px;color:var(--ink)}
.field{position:absolute;left:172px;width:256px;height:45px;background:var(--field-bg);box-shadow:0 2px 3px rgba(0,0,0,.25)}
.field .caret{position:absolute;right:14px;top:19px}
.btn-next{position:absolute;left:341px;top:487px;width:87px;height:34px;background:var(--btn);color:#d9e9f2;font-size:15px;display:flex;align-items:center;justify-content:center;border-radius:2px}
.submenu{position:absolute;background:var(--royal)}
.submenu.level1{left:216px;top:85px;width:186px;height:217px}
.submenu.level1 .item{height:53px;display:flex;align-items:center;justify-content:space-between;padding:0 34px 0 32px;color:var(--white);font-size:16.5px}
.submenu.level1 .item.open{background:var(--sky)}
.submenu.level2{left:401px;top:191px;width:199px;height:338px;background:var(--sky);padding-top:8px}
.submenu.level2 .item{height:39.2px;display:flex;align-items:center;justify-content:space-between;padding:0 24px;color:var(--white);font-size:14.5px;white-space:nowrap}
.footer{position:absolute;left:218px;top:770px;width:982px;height:47px;background:var(--footer);color:#d5dbe4;font-size:12px;display:flex;align-items:center;justify-content:center;padding-right:20px}
</style>
</head>
<body>
<header class="topbar">
  <div class="welcome">Welcome Admin</div>
  <div class="meta">
    <span>|</span><span>Tuesda October 03 ,2017</span><span>|</span>
    <svg width="16" height="16" viewBox="0 0 16 16"><path d="M8 1a1.2 1.2 0 0 1 1.2 1.2v.5A4.5 4.5 0 0 1 12.5 7v3.5l1.5 2H2l1.5-2V7a4.5 4.5 0 0 1 3.3-4.3v-.5A1.2 1.2 0 0 1 8 1zm-1.8 12.5h3.6a1.8 1.8 0 0 1-3.6 0z" fill="#2b3340"/></svg>
    <span>|</span>
    <svg width="15" height="14" viewBox="0 0 15 14"><path d="M1 2h5v2H3v6h3v2H1zM8 3l5 4-5 4V8.5H5v-3h3z" fill="#2b3340"/></svg>
  </div>
</header>

<nav class="sidebar">
  <div class="brand"><span class="name">Tallyview</span></div>
  <div class="nav-row active"><div class="icon"><svg width="18" height="18" viewBox="0 0 18 18"><circle cx="9" cy="5" r="4" fill="#fff"/><path d="M1 17c0-5 3.5-7 8-7s8 2 8 7z" fill="#fff"/></svg></div><div class="label">Admin<svg class="chev" viewBox="0 0 8 12"><path d="M1.5 1l5 5-5 5" stroke="#fff" stroke-width="2" fill="none"/></svg></div></div>
  <div class="nav-row"><div class="icon"><svg width="18" height="16" viewBox="0 0 18 16"><path d="M3 2h12l3 7v5H0V9zm-1 7h4l1 2h4l1-2h4l-2-5H4z" fill="#fff"/></svg></div><div class="label">Management<svg class="chev" viewBox="0 0 8 12"><path d="M1.5 1l5 5-5 5" stroke="#fff" stroke-width="2" fill="none"/></svg></div></div>
  <div class="nav-row"><div class="icon"><svg width="18" height="16" viewBox="0 0 18 16"><path d="M9 1l8 7h-2.5v7h-4v-4.5h-3V15h-4V8H1z" fill="#fff"/></svg></div><div class="label">Property Search<svg class="chev" viewBox="0 0 8 12"><path d="M1.5 1l5 5-5 5" stroke="#fff" stroke-width="2" fill="none"/></svg></div></div>
  <div class="nav-row"><div class="icon"><svg width="22" height="18" viewBox="0 0 22 18"><rect x="1" y="1" width="20" height="12" fill="none" stroke="#fff" stroke-width="2"/><rect x="8" y="14" width="6" height="2" fill="#fff"/><rect x="5" y="16" width="12" height="2" fill="#fff"/></svg></div><div class="label">Intel<svg class="chev" viewBox="0 0 8 12"><path d="M1.5 1l5 5-5 5" stroke="#fff" stroke-width="2" fill="none"/></svg></div></div>
  <div class="nav-row"><div class="icon"><svg width="16" height="20" viewBox="0 0 16 20"><path d="M0 0h10l6 6v14H0z" fill="#fff"/><path d="M3 9h10M3 12h10M3 15h10" stroke="#062650" stroke-width="1.4"/></svg></div><div class="label">Planning<svg class="chev" viewBox="0 0 8 12"><path d="M1.5 1l5 5-5 5" stroke="#fff" stroke-width="2" fill="none"/></svg></div></div>
</nav>

<section class="panel">
  <div class="panel-head">Search</div>
  <div class="field" style="top:81px"></div>
  <div class="field" style="top:126px"></div>
  <div class="field-label" style="top:186px">Search ID</div>
  <div class="field" style="top:174px"></div>
  <div class="field-label" style="top:249px">Search Product</div>
  <div class="field" style="top:236px"></div>
  <div class="field-label" style="top:311px">Divisions</div>
  <div class="field" style="top:298px"><svg class="caret" width="9" height="5" viewBox="0 0 9 5"><path d="M0 0h9L4.5 5z" fill="#222"/></svg></div>
  <div class="field-label" style="top:373px">Regions</div>
  <div class="field" style="top:360px"></div>
  <div class="field-label" style="top:434px">Areas</div>
  <div class="field" style="top:422px"></div>
  <div class="btn-next">Next »</div>
</section>

<div class="submenu level1">
  <div class="item">Registration<svg class="chev" viewBox="0 0 8 12"><path d="M1.5 1l5 5-5 5" stroke="#fff" stroke-width="2" fill="none"/></svg></div>
  <div class="item">User Access<svg class="chev" viewBox="0 0 8 12"><path d="M1.5 1l5 5-5 5" stroke="#fff" stroke-width="2" fill="none"/></svg></div>
  <div class="item open">Setup<svg class="chev" viewBox="0 0 8 12"><path d="M1.5 1l5 5-5 5" stroke="#fff" stroke-width="2" fill="none"/></svg></div>
  <div class="item">Data imports<svg class="chev" viewBox="0 0 8 12"><path d="M1.5 1l5 5-5 5" stroke="#fff" stroke-width="2" fill="none"/></svg></div>
</div>

<div class="submenu level2">
  <div class="item">Market Segments<svg class="chev" viewBox="0 0 8 12"><path d="M1.5 1l5 5-5 5" stroke="#fff" stroke-width="2" fill="none"/></svg></div>
  <div class="item">Banquet &amp; Catering<svg class="chev" viewBox="0 0 8 12"><path d="M1.5 1l5 5-5 5" stroke="#fff" stroke-width="2" fill="none"/></svg></div>
  <div class="item">Outlets/F&amp;B Service<svg class="chev" viewBox="0 0 8 12"><path d="M1.5 1l5 5-5 5" stroke="#fff" stroke-width="2" fill="none"/></svg></div>
  <div class="item">Other Income<svg class="chev" viewBox="0 0 8 12"><path d="M1.5 1l5 5-5 5" stroke="#fff" stroke-width="2" fill="none"/></svg></div>
  <div class="item">Impact Dates<svg class="chev" viewBox="0 0 8 12"><path d="M1.5 1l5 5-5 5" stroke="#fff" stroke-width="2" fill="none"/></svg></div>
  <div class="item">Inventory<svg class="chev" viewBox="0 0 8 12"><path d="M1.5 1l5 5-5 5" stroke="#fff" stroke-width="2" fill="none"/></svg></div>
  <div class="item">Geo/Location<svg class="chev" viewBox="0 0 8 12"><path d="M1.5 1l5 5-5 5" stroke="#fff" stroke-width="2" fill="none"/></svg></div>
  <div class="item">Distribution Channels<svg class="chev" viewBox="0 0 8 12"><path d="M1.5 1l5 5-5 5" stroke="#fff" stroke-width="2" fill="none"/></svg></div>
</div>

<footer class="footer">Copyright © 2017. All Rights Reserved</footer>
</body>
</html>
```